Modern home page design for a Dental Surgery

- This design will have a 5 day deadline only.

- The design must be based around the attached HPID (home page information design) called LUMA HPID. I've attached Word and PDF versions - these are the same. The table boxes are just for approximate placement of information – you DON'T have to make it look exactly like this. All fonts used in the HPID are only examples - you can use any Google font you wish.

- Information only is in orange text. Copy to go on the design in black text. Some instructions are in the HPID. Please be creative!

- The design needs to be modern. Colours are to be black and white with grey and blue like the logo colours. Background white please.

- I've provided the images for the galleries - they are labelled and will match the name in the HPID.

- I've provided icons for the items below the gallery - the name of the image will match the subheading for each section. You can use other icons if you want to.

- This is a website that is an example of what we like. Please DON'T copy this exactly though!
http://brightmolarclinic.example.co.nz/

Width of content will be 1100 pixels when implemented as a web page. Header height (without nav bar) 150-160 pixels.

If your design is chosen the winning PSD file will have to be provided as follows…
1. Canvas size of 2000px x 2000px - 72ppi in Adobe Photoshop (CS5 compatible)
2. Width of content section is 1100px wide - centered in the canvas
3. Any button rollovers/hovers in the PSD as hidden layers.
4. All fonts used must be Google fonts (except for the fonts in the header at the top of the page).
5. You will need to supply the chosen home page plus one example page (example page as a style guide for how all other pages will look). Example page is only the header and navigational bar at the top, an empty sector in the middle with a column (180 px wide) which can be left or right aligned which means the main sector is 920 pixels wide, and then the footer at the bottom of the page
Updates

Hi Designers, The 1st posted deadline for this project was incorrect; please note new deadline for November 22.

Target Market(s)

all ages that need dental care

Industry/Entity Type

Dental

Number of Pages Required

1 page

Font styles to use
Sans Serif

Requirements
Must have
• modern clean design - as per the Project Description
Should not have
• should not be cluttered. Just because I use tables to show information placement on the HPID - you do NOT have to use boxes around information in the design.

```html
<!DOCTYPE html>
<html lang="en">
<head>
<meta charset="utf-8">
<title>Harbour Dental Care – Kowhai Bay</title>
<link href="https://fonts.googleapis.com/css2?family=Roboto:wght@300;400;500;700&family=Roboto+Condensed:wght@300;400&display=swap" rel="stylesheet">
<style>
:root{
  --blue:#1f4f7f;
  --blue-dark:#17395b;
  --blue-text:#2b5f8f;
  --ink:#333;
  --muted:#555;
  --footer-bg:#141414;
  --footer-link:#2d6aa0;
  --footer-text:#8a8a8a;
  --bar:#1b3d5e;
  --line:#9a9a9a;
}
*{box-sizing:border-box;margin:0;padding:0}
html,body{width:682px;height:1200px;overflow:hidden;background:#fff}
body{position:relative;font-family:'Roboto',Arial,sans-serif;color:var(--ink)}
.abs{position:absolute}
.header{left:0;top:0;width:682px;height:58px;background:linear-gradient(#fff,#ececec)}
.brand{left:66px;top:12px;width:58px;height:36px;border:1.5px solid #9aa4ad;border-radius:50%;display:flex;align-items:center;justify-content:center;font-size:8px;font-weight:400;color:var(--blue-text)}
.locale{left:305px;top:22px;font-size:10.5px;font-weight:400;color:#333;white-space:nowrap}
.locale small{font-size:7px;font-weight:300;margin-left:2px}
.locale .sep{display:inline-block;width:1px;height:12px;background:#333;margin:0 5px;vertical-align:middle}
.phone{left:503px;top:19px;font-size:14.5px;font-weight:300;color:#444}
.nav{left:0;top:58px;width:682px;height:36px;background:linear-gradient(var(--blue),var(--blue-dark))}
.nav a{position:absolute;top:12px;font-size:9.6px;font-weight:300;color:#fff;text-decoration:none;white-space:nowrap}
.hero{left:0;top:94px;width:682px;height:284px;background:linear-gradient(90deg,#eceef0 0%,#e2e5e8 35%,#d9cbbf 52%,#c9a990 64%,#b9b2ab 78%,#c4cad1 100%)}
.hero-title{left:83px;top:228px;font-size:19px;font-weight:300;color:#2c4a66}
.hero-cta{left:83px;top:253px;font-size:21px;font-weight:700;color:#2c4a66}
.heading{font-size:20px;font-weight:300;color:var(--blue-text);white-space:nowrap}
.heading.sm{font-size:14.5px}
.copy{font-size:7.6px;line-height:11.5px;font-weight:300;color:var(--muted)}
.btn{display:flex;align-items:center;justify-content:center;height:26px;border-radius:3px;color:#fff;font-size:9.6px;font-weight:300;font-family:'Roboto Condensed',Arial,sans-serif;background:linear-gradient(#3b3b3b,#1c1c1c)}
.btn.blue{background:linear-gradient(#2f6496,#173d63)}
.emergency{left:0;top:641px;width:682px;height:284px;background:linear-gradient(100deg,#a9cbe0 0%,#c9d4de 30%,#d8c7b3 55%,#d2b89f 68%,#e3d2c0 78%,#f0ece8 100%)}
.portrait{left:470px;top:641px;width:212px;height:284px;background:radial-gradient(ellipse at 60% 40%,rgba(232,196,168,.9) 0%,rgba(230,205,170,.5) 45%,rgba(240,236,232,0) 75%)}
.assoc-label{left:94px;top:862px;font-size:17px;font-weight:500;color:#fff}
.badge{top:851px;width:98px;height:49px;background:#fff;border:1px solid #ccc;display:flex;align-items:center;justify-content:center}
.footer{left:0;top:925px;width:682px;height:237px;background:var(--footer-bg)}
.fcol{position:absolute;list-style:none;font-size:7.2px;line-height:13.6px;font-weight:300;color:var(--footer-text);white-space:nowrap}
.fcol .lnk{color:var(--footer-link)}
.fcol .i1{padding-left:6px}
.fcol .i2{padding-left:14px}
.ftitle{font-size:9px;font-weight:300;color:var(--footer-link)}
.bar{left:0;top:1162px;width:682px;height:38px;background:var(--bar)}
.social{top:1170px;width:18px;height:18px;border-radius:50%;background:#e4e4e4}
.copyright{left:479px;top:1178px;font-size:7px;color:#fff}
</style>
</head>
<body>
<header class="abs header"></header>
<div class="abs brand">LUMA Group</div>
<div class="abs locale">Kowhai Bay<span class="sep"></span><small>Family Dentistry&nbsp; KOWHAI BAY</small></div>
<div class="abs phone">PH: 04 555 0187</div>

<nav class="abs nav">
  <a style="left:108px">Home</a><a style="left:152px">About</a><a style="left:196px">What We Do</a><a style="left:266px">Why Choose Us</a><a style="left:348px">Services</a><a style="left:400px">Costs</a><a style="left:441px">Appointment</a><a style="left:515px">Contact / Map</a>
</nav>

<section class="abs hero" role="img" aria-label="Photo of a dentist examining a young girl in the dental chair"></section>
<div class="abs hero-title">Need an expert caring dentist?</div>
<div class="abs hero-cta">Call us!</div>
<svg class="abs" style="left:95px;top:320px" width="42" height="30" viewBox="0 0 42 30"><path d="M15 1 L2 15 L15 29 M27 1 L40 15 L27 29" fill="none" stroke="#555" stroke-width="1.2"/></svg>

<svg class="abs" style="left:82px;top:394px" width="24" height="28" viewBox="0 0 24 28"><path d="M6 2c3 0 4 2 6 2s3-2 6-2c3 0 4 3 3 6l-2 8c0 2-2 2-2 0l-1-4-4 0-1 4c0 2-2 2-2 0L3 8C2 5 3 2 6 2z" fill="#3a8fd0"/><circle cx="12" cy="23" r="3" fill="none" stroke="#333" stroke-width="1.5"/></svg>
<div class="abs heading" style="left:113px;top:396px">What We Do</div>
<p class="abs copy" style="left:80px;top:429px;width:246px">The Harbour Dental Care offer a wide range of dental services including diagnostics, orthodontics, dentures, oral surgery, and periodontal, root canal and cosmetic dentistry.</p>
<div class="abs btn blue" style="left:80px;top:471px;width:63px">MORE</div>

<svg class="abs" style="left:352px;top:398px" width="18" height="26" viewBox="0 0 18 26"><path d="M4 1c3 0 3 2 5 2s2-2 5-2c3 0 4 3 3 6l-3 16c-1 2-2 2-2 0l-1-6h-4l-1 6c0 2-2 2-2 0L1 7C0 4 1 1 4 1z" fill="none" stroke="#2b5f8f" stroke-width="1.4"/></svg>
<div class="abs heading" style="left:381px;top:398px">How much does it Cost?</div>
<p class="abs copy" style="left:354px;top:429px;width:255px">Find out estimates of how much each dental procedure costs. (Exact prices will be discussed with you after consultation depending on your specific dental requirements.)</p>
<div class="abs btn" style="left:354px;top:472px;width:63px">COSTS</div>

<svg class="abs" style="left:0;top:395px" width="682" height="240">
  <line x1="338" y1="5" x2="338" y2="113" stroke="var(--line)" stroke-dasharray="2 2"/>
  <line x1="80" y1="120" x2="598" y2="120" stroke="var(--line)" stroke-dasharray="2 2"/>
  <circle cx="338" cy="121" r="4" fill="#fff" stroke="#b8c7d3"/>
  <line x1="248" y1="128" x2="248" y2="235" stroke="var(--line)" stroke-dasharray="2 2"/>
  <line x1="431" y1="128" x2="431" y2="235" stroke="var(--line)" stroke-dasharray="2 2"/>
</svg>

<svg class="abs" style="left:78px;top:532px" width="24" height="20" viewBox="0 0 24 20"><ellipse cx="11" cy="14" rx="10" ry="4" fill="none" stroke="#bcd"/><path d="M4 13 L20 3" stroke="#2b5f8f" stroke-width="3" stroke-linecap="round"/></svg>
<div class="abs heading sm" style="left:103px;top:533px">Make an Appointment</div>
<p class="abs copy" style="left:80px;top:556px;width:165px">Two convenient locations in Ridgefield and Kowhai Bay offer dental services for all ages. Take a moment to book your appointment</p>
<div class="abs btn" style="left:80px;top:602px;width:80px">APPOINTMENT</div>

<svg class="abs" style="left:262px;top:531px" width="16" height="22" viewBox="0 0 18 26"><path d="M4 1c3 0 3 2 5 2s2-2 5-2c3 0 4 3 3 6l-3 16c-1 2-2 2-2 0l-1-6h-4l-1 6c0 2-2 2-2 0L1 7C0 4 1 1 4 1z" fill="none" stroke="#2b5f8f" stroke-width="1.5"/></svg>
<div class="abs heading sm" style="left:283px;top:533px">Your First Consultation</div>
<p class="abs copy" style="left:262px;top:556px;width:165px">Want to know what will happen in your first consultation? Check out our first dental consultation process.</p>
<div class="abs btn" style="left:262px;top:602px;width:108px">FIRST CONSULTATION</div>

<svg class="abs" style="left:445px;top:531px" width="17" height="22" viewBox="0 0 17 22"><rect x="1" y="2" width="15" height="19" rx="1" fill="#fff" stroke="#2b5f8f" stroke-width="1.5"/><rect x="5" y="0.5" width="7" height="3" fill="#2b5f8f"/><path d="M4 8h9M4 12h9M4 16h6" stroke="#3a8fd0"/></svg>
<div class="abs heading sm" style="left:468px;top:533px">Application Form</div>
<p class="abs copy" style="left:445px;top:556px;width:170px">Save time and fill in an online application form (or download, print out and complete) before your first visit.</p>
<div class="abs btn" style="left:444px;top:602px;width:80px">APPOINTMENT</div>

<section class="abs emergency" role="img" aria-label="Soft blurred blue and warm background"></section>
<div class="abs portrait" role="img" aria-label="Photo of a woman holding her cheek with toothache"></div>
<svg class="abs" style="left:92px;top:724px" width="18" height="26" viewBox="0 0 18 26"><path d="M4 1c3 0 3 2 5 2s2-2 5-2c3 0 4 3 3 6l-3 16c-1 2-2 2-2 0l-1-6h-4l-1 6c0 2-2 2-2 0L1 7C0 4 1 1 4 1z" fill="none" stroke="#1f3f5f" stroke-width="1.4"/></svg>
<div class="abs heading" style="left:120px;top:723px;font-size:21px;color:#1f3f5f">Is this an emergency?</div>
<p class="abs copy" style="left:94px;top:762px;width:340px;color:#222;font-weight:400">Lorem ipsum dolor sit amet, consectetur adipiscing elit, sed do eiusmod tempor incididunt ut labore et dolore magna aliqua. Ut enim ad minim veniam</p>
<div class="abs btn" style="left:94px;top:797px;width:120px">CONTACT IMMEDIATELY</div>
<div class="abs assoc-label">Associations</div>
<div class="abs badge" style="left:201px"><svg width="60" height="38"><ellipse cx="30" cy="19" rx="29" ry="18" fill="#1d6a6e"/></svg></div>
<div class="abs badge" style="left:310px"><svg width="64" height="30"><rect x="2" y="4" width="60" height="22" fill="#e6e6e6"/></svg></div>

<footer class="abs footer">
  <ul class="fcol" style="left:93px;top:28px">
    <li class="lnk">Home</li><li class="lnk" style="margin-top:5px">About</li><li class="i1" style="line-height:10px">- Team</li><li class="i1" style="line-height:10px">- Registration form</li><li class="lnk" style="margin-top:3px">What We Do</li><li class="lnk" style="margin-top:5px">Why Choose Us</li><li class="i1" style="margin-top:3px">- Testimonials</li><li class="lnk" style="margin-top:3px">Costs</li><li class="lnk" style="margin-top:5px">Appointment</li><li class="lnk" style="margin-top:5px">Contact / Map</li>
  </ul>
  <div class="ftitle abs" style="left:189px;top:31px">Services</div>
  <ul class="fcol" style="left:189px;top:50px">
    <li class="lnk">Restorative Dentistry</li><li class="i1">▸ Preventative</li><li class="i2">▸ Fissure Sealants</li><li class="i2">▸ Mouthguards</li><li class="i2">▸ Bite Splints</li><li class="i1">▸ Fillings</li><li class="i2">▸Amalgams, Composites (white</li><li class="i2">fillings)</li><li class="i2">▸Porcelain &amp; Gold</li><li class="i1">▸ Crown &amp; Bridge Treatment</li><li class="i1">▸ Implants</li>
  </ul>
  <ul class="fcol" style="left:337px;top:50px">
    <li class="lnk">Oral Surgery</li><li class="i1">▸ Extractions</li><li class="i1">▸ Minor Impacted Wisdom Teeth</li><li class="lnk" style="margin-top:3px">Periodontal (gum) Care</li><li class="i1">▸ Hygiene Services</li><li class="i1">▸ Minor Periodontal Surgery</li><li class="i1">▸ Preventative Services</li><li class="lnk" style="margin-top:3px">Root Canal Therapy</li><li class="lnk">Cosmetic</li><li class="i1">▸ Porcelain Veneers</li><li class="i1">▸ Power Bleaching (in surgery</li><li class="i2">teeth whitening)</li>
  </ul>
  <ul class="fcol" style="left:474px;top:50px">
    <li class="lnk">Dentures</li><li class="lnk">Orthodontics</li><li class="lnk">Children &amp; pre-schoolers</li><li class="i1">▸ Free Secondary School Dentistry</li><li class="i2">▸ Free Dental Care Under 18</li><li class="i1">▸ Pre-school Dentistry</li><li class="lnk">Oral Care Products</li><li class="lnk">Diagnostic Dentistry</li><li class="i1">▸ Digital X-rays</li><li class="i1">▸ Panoramic X-rays</li><li class="i1">▸ Intra-oral photography &amp; Camera</li><li class="i1">▸ Laser Cavity Detection</li>
  </ul>
</footer>
<div class="abs bar"></div>
<div class="abs social" style="left:93px"></div>
<div class="abs social" style="left:116px"></div>
<div class="abs social" style="left:139px"></div>
<div class="abs social" style="left:162px"></div>
<div class="abs social" style="left:185px"></div>
<div class="abs copyright">© 2014.www.harbourdental.example</div>
</body>
</html>
```